Thank you cards for online orders

We have a logo that is attached and I'd for it to be used to make a thank you card that will give our clients some info on product care as well as refund/exchange policy. so maybe a small package that includes a thank you card, and policy details
Updates

Sick

Target Market(s)

Females for 20-70

```html
<!DOCTYPE html>
<html lang="en">
<head>
<meta charset="utf-8">
<title>Lumira – Thank You Card Set</title>
<link rel="stylesheet" href="https://fonts.googleapis.com/css2?family=Nunito+Sans:wght@300;400&family=Kaushan+Script&display=swap">
<style>
  :root {
    --canvas: #dcdbd8;
    --white: #ffffff;
    --lime: #8dc63f;
    --lime-text: #7bb83a;
    --leaf: #3f7a3a;
    --forest: #004438;
    --sage: #95a594;
    --sage-dark: #7f9281;
    --grey-text: #868686;
  }
  * { margin: 0; padding: 0; box-sizing: border-box; }
  html, body {
    width: 1200px; height: 1200px; overflow: hidden;
    background: var(--canvas);
    font-family: "Nunito Sans", "Helvetica Neue", Arial, sans-serif;
  }
  .set { position: relative; width: 1200px; height: 1200px; }
  .card {
    position: absolute; left: 246px; width: 704px; height: 469px;
    background: var(--white); overflow: hidden;
  }
  .card-shadow {
    position: absolute; left: 300px; width: 600px; height: 30px;
    background: radial-gradient(ellipse at center, rgba(0,0,0,0.22) 0%, rgba(0,0,0,0) 70%);
  }
  .card-care { top: 80px; }
  .card-thanks { top: 610px; }
  .card-shape { position: absolute; inset: 0; width: 704px; height: 469px; }

  .care-title {
    position: absolute; left: 29px; top: 34px; width: 177px; height: 32px;
    border-top: 2px solid var(--lime); border-bottom: 2px solid var(--lime);
    font-weight: 300; font-size: 23px; line-height: 28px; letter-spacing: 0.3px;
    color: var(--grey-text); white-space: nowrap;
  }
  .care-body {
    position: absolute; left: 29px; top: 94px; width: 360px;
    font-weight: 300; font-size: 11.3px; line-height: 14.4px; color: var(--lime-text);
  }
  .care-body p + p { margin-top: 14.4px; }
  .policy-title {
    position: absolute; left: 29px; top: 342px;
    font-weight: 300; font-size: 11px; color: var(--grey-text); letter-spacing: 0.2px;
  }
  .policy-body {
    position: absolute; left: 32px; top: 370px; width: 355px;
    font-weight: 300; font-size: 8.6px; line-height: 11.6px; color: var(--lime-text);
  }
  .brand-name {
    position: absolute; font-weight: 300; font-size: 24px; letter-spacing: 3px;
    color: var(--lime); white-space: nowrap; transform: translateX(-50%);
  }
  .card-care .brand-name { left: 588px; top: 28px; }
  .card-thanks .brand-name { left: 567px; top: 396px; }
  .thanks-title {
    position: absolute; left: 190px; top: 150px; width: 440px; text-align: center;
    font-family: "Kaushan Script", cursive; font-size: 86px; line-height: 1;
    color: var(--sage); transform: rotate(-4deg);
    text-shadow: 3px 5px 6px rgba(0,0,0,0.45);
  }
</style>
</head>
<body>
<main class="set">

  <section class="card card-care">
    <svg class="card-shape" viewBox="0 0 704 469" aria-hidden="true">
      <defs>
        <linearGradient id="careGreen" x1="0" y1="0" x2="1" y2="0">
          <stop offset="0" stop-color="#2f6b3a"/>
          <stop offset="1" stop-color="#8dc63f"/>
        </linearGradient>
        <linearGradient id="careWhite" x1="0" y1="0" x2="0" y2="1">
          <stop offset="0.5" stop-color="#ffffff"/>
          <stop offset="1" stop-color="#efefef"/>
        </linearGradient>
      </defs>
      <rect width="704" height="469" fill="url(#careWhite)"/>
      <path d="M362 0 C500 60 590 200 520 360 C505 400 495 440 480 469 L704 469 L704 0 Z" fill="var(--sage)"/>
      <path d="M390 0 C520 60 610 210 545 360 C530 400 520 440 510 469 L704 469 L704 0 Z" fill="url(#careGreen)"/>
      <path d="M430 76 C530 170 560 310 446 469 L478 469 C575 320 540 170 430 76 Z" fill="var(--lime)"/>
    </svg>
    <h2 class="care-title">PRODUCT CARE</h2>
    <div class="care-body">
      <p>Lorem ipsum dolor sit amet, consectetuer adipiscing elit, sed diam nonummy nibh euismod tincidunt ut laoreet dolore magna aliquam erat volutpat. Ut wisi enim ad minim veniam, quis nostrud exerci tation ullamcorper suscipit lobortis nisl ut aliquip ex ea commodo consequat. Duis autem vel eum iriure dolor in hendrerit in vulputate velit esse molestie consequat, vel illum dolore eu feugiat nulla facilisis at vero eros et accumsan et iusto odio dignissim qui blandit praesent luptatum zzril delenit augue duis dolore te feugait nulla facilisi.</p>
      <p>Lorem ipsum dolor sit amet, cons ectetuer adipiscing elit, sed diam nonummy nibh euismod tincidunt ut laoreet dolore magna aliquam erat volutpat. Ut wisi enim ad minim veniam, quis nostrud exerci tation ullamcorper suscipit lobortis nisl ut aliquip ex ea commodo consequat.</p>
    </div>
    <h3 class="policy-title">REFUND / EXCHANGE POLICY</h3>
    <p class="policy-body">Lorem ipsum dolor sit amet, consectetuer adipiscing elit, sed diam nonummy nibh euismod tincidunt ut laoreet dolore magna aliquam erat volutpat. Ut wisi enim ad minim veniam, quis nostrud exerci tation ullamcorper suscipit lobortis nisl ut aliquip ex ea commodo consequat. Duis autem vel eum iriure dolor in hendrerit in vulputate velit esse molestie consequat, vel illum dolore eu feugiat nulla facilisis</p>
    <div class="brand-name">LUMIRA</div>
  </section>
  <div class="card-shadow" style="top:552px"></div>

  <section class="card card-thanks">
    <svg class="card-shape" viewBox="0 0 704 469" aria-hidden="true">
      <defs>
        <linearGradient id="thanksWhite" x1="0" y1="0" x2="0" y2="1">
          <stop offset="0.3" stop-color="#ffffff"/>
          <stop offset="1" stop-color="#e6e6e6"/>
        </linearGradient>
        <linearGradient id="thanksLime" x1="0" y1="0" x2="1" y2="1">
          <stop offset="0" stop-color="#8aa883"/>
          <stop offset="0.5" stop-color="#93c24a"/>
        </linearGradient>
        <radialGradient id="thanksShade" cx="0.15" cy="0.5" r="0.5">
          <stop offset="0" stop-color="#00241d" stop-opacity="0.7"/>
          <stop offset="1" stop-color="#00241d" stop-opacity="0"/>
        </radialGradient>
      </defs>
      <rect width="704" height="469" fill="url(#thanksWhite)"/>
      <path d="M522 0 C300 10 110 70 78 230 C68 320 100 420 130 469 L704 469 L704 0 Z" fill="var(--sage)"/>
      <path d="M90 170 C80 280 120 400 186 469 L704 469 L704 0 L400 0 C250 20 120 80 90 170 Z" fill="url(#thanksLime)"/>
      <path d="M520 0 C320 20 150 80 100 200 C80 290 200 420 418 469 L704 469 L704 0 Z" fill="var(--forest)"/>
      <path d="M520 0 C320 20 150 80 100 200 C80 290 200 420 418 469 L704 469 L704 0 Z" fill="url(#thanksShade)"/>
    </svg>
    <h1 class="thanks-title">Thank you!</h1>
    <div class="brand-name">LUMIRA</div>
  </section>
  <div class="card-shadow" style="top:1082px"></div>

</main>
</body>
</html>
```